Dalton Perriwether breaking. Or D. Perriwether breaking

I break in and train horses, any age any bread of horse, for any disaplin. I need a business card that is simple but effective, in the way of looking professional. I would like a horse on my card, preferably a horse without a rider. I also pre train horse, younge horses that need a bit of riding before they go into serious work, and prepare yearlings for sale.

Reason: This is for my boyfriend, and I really want it to be perfect and impressive!

Target Market(s)

Thoroughbred race horse trainers, horse industrie people.

Industry/Entity Type

Business

Contact Information for Business Card

Dalton Perriwether horse breaking, "WOLLOMBEE" Armidale, give your horse the right start to any career. dperri@mailzone.com.au, 0481392067. Horse breaking~pre-training~sale preparation

```html
<!DOCTYPE html>
<html lang="en">
<head>
<meta charset="utf-8">
<title>Dalton Perriwether horse breaking</title>
<link rel="stylesheet" href="https://fonts.googleapis.com/css2?family=Bodoni+Moda:opsz,wght@6..96,400;6..96,700&display=swap">
<style>
  :root {
    --sky-top: #361611;
    --sky-mid: #562117;
    --sky-low: #7e331c;
    --horizon: #b5552a;
    --sun-glow: rgba(214, 120, 60, 0.55);
    --ground: #120907;
    --footer-band: #17110f;
    --silhouette: rgba(20, 8, 6, 0.55);
    --rule: #6d6562;
    --ink: #fbf6f1;
  }
  html, body {
    margin: 0;
    padding: 0;
    overflow: hidden;
    background: #000;
  }
  .card {
    position: relative;
    width: 1200px;
    height: 741px;
    overflow: hidden;
    font-family: "Bodoni Moda", "Didot", serif;
    color: var(--ink);
  }
  .card__scene {
    position: absolute;
    inset: 0;
    background:
      radial-gradient(ellipse 110px 70px at 875px 622px, var(--sun-glow) 0%, rgba(214,120,60,0) 100%),
      linear-gradient(180deg,
        var(--sky-top) 0%,
        var(--sky-mid) 40%,
        var(--sky-low) 68%,
        var(--horizon) 83%,
        var(--ground) 84%,
        var(--ground) 94%,
        var(--footer-band) 94.2%,
        var(--footer-band) 100%);
  }
  .card__horse {
    position: absolute;
    left: 60px;
    top: 20px;
    width: 680px;
    height: 580px;
    border-radius: 40%;
    background: radial-gradient(ellipse at 50% 50%, var(--silhouette) 0%, rgba(20,8,6,0.35) 55%, rgba(20,8,6,0) 75%);
  }
  .card__rule {
    position: absolute;
    left: 0;
    right: 0;
    top: 699px;
    height: 1px;
    background: var(--rule);
  }
  .card__line {
    position: absolute;
    left: 0;
    width: 100%;
    margin: 0;
    text-align: center;
    line-height: 1;
    white-space: nowrap;
    font-weight: 400;
  }
  .card__name,
  .card__trade {
    font-size: 92px;
    font-weight: 700;
    letter-spacing: -0.5px;
  }
  .card__name  { top: 33px; left: 9px; }
  .card__trade { top: 148px; left: 9px; }
  .card__property {
    top: 276px;
    left: 3px;
    font-size: 45px;
    letter-spacing: 0.5px;
  }
  .card__tagline {
    top: 330px;
    left: -8px;
    font-size: 48px;
    letter-spacing: 0.5px;
  }
  .card__email {
    top: 410px;
    left: -8px;
    font-size: 80px;
  }
  .card__phone {
    top: 508px;
    left: 5px;
    font-size: 78px;
  }
  .card__services {
    top: 623px;
    left: -18px;
    font-size: 37px;
    letter-spacing: 0.8px;
  }
</style>
</head>
<body>
  <main class="card">
    <div class="card__scene" role="img" aria-label="Red sunset sky with the sun setting over a dark horizon"></div>
    <div class="card__horse" role="img" aria-label="Dark silhouette of a galloping horse without a rider"></div>
    <div class="card__rule"></div>

    <h1 class="card__line card__name">Dalton Perriwether</h1>
    <p class="card__line card__trade">horse breaking</p>
    <p class="card__line card__property">"WOLLOMBEE" Armidale</p>
    <p class="card__line card__tagline">give your horse the right start to any career</p>
    <p class="card__line card__email">dperri@mailzone.com.au</p>
    <p class="card__line card__phone">0481392067</p>
    <p class="card__line card__services">Horse breaking~pre-training~sale preparation</p>
  </main>
</body>
</html>
```